Home based bath & shave business wants to redesign labels

I would like to have new labels designed to fit the body lotion and bath oil bottles. We want them similar but different. The key ingredient for all of Ferrucci's Bath & Shave products is olive oil.

You are free to change colors. I have attached our logo and current labels. The current labels just don't look right to me (pictures attached). I like the script font, but am willing to entertain another. I have our logo in several formats and the font, should you want it.

Target Market(s)

Women

Industry/Entity Type

Business

Font styles to use
Decorative
Script

Requirements
Must have
• Both product labels must include our logo.The logo must stay the same though to make it work with the label, you can change the color if needed.
• It should be a vertical label.
• The bottle used is a 8 oz Clear PET Tapered Naples Oval Bottle (I have attached pictures) and its dimensions are:
• Length 2.548 in / 6.472 cm
• Width 1.479 in / 3.757 cm
• Height 6.639 in / 16.863 cm

```html
<!DOCTYPE html>
<html lang="en">
<head>
<meta charset="utf-8">
<title>Ferrucci's Bath &amp; Shave – Labels</title>
<link href="https://fonts.googleapis.com/css2?family=Great+Vibes&family=Open+Sans:wght@400;600;700&display=swap" rel="stylesheet">
<style>
  :root {
    --canvas: #ffffff;
    --frame: #f7941d;
    --tab: #ffffff;
    --brand-red: #e8262a;
    --title: #ffffff;
    --leaf-light: #9bd14a;
    --leaf-mid: #5aa82a;
    --leaf-deep: #2f6e1a;
    --olive-dark: #4a3a2e;
    --lotion-blue: #2a86c6;
    --lotion-blue-deep: #1f78b8;
    --cream: #f3ecdc;
    --cream-shade: #e2d6bd;
    --ink-blue: #2a86c6;
  }
  * { box-sizing: border-box; margin: 0; padding: 0; }
  html, body {
    width: 1200px; height: 1041px; overflow: hidden;
    background: var(--canvas);
    font-family: "Open Sans", Arial, sans-serif;
  }
  .canvas { position: relative; width: 1200px; height: 1041px; }

  .label {
    position: absolute; top: 39px;
    width: 503px; height: 922px;
    border: 5px solid var(--frame);
    border-radius: 4px;
    overflow: hidden;
  }
  .label--oil { left: 39px; }
  .label--lotion { left: 611px; }

  .label__photo { position: absolute; inset: 0; }
  .label--oil .label__photo {
    background:
      linear-gradient(180deg, transparent 78%, rgba(74,58,46,0.85) 92%, var(--olive-dark) 100%),
      radial-gradient(ellipse at 70% 30%, var(--leaf-light), transparent 60%),
      linear-gradient(160deg, var(--leaf-light) 0%, var(--leaf-mid) 45%, var(--leaf-deep) 100%);
  }
  .label--lotion .label__photo {
    background: linear-gradient(180deg, var(--lotion-blue), var(--lotion-blue-deep));
  }

  .label__swirl { position: absolute; left: 0; top: 0; width: 493px; height: 912px; }

  .brand-tab {
    position: absolute; top: -5px; left: 66px;
    width: 360px; height: 266px;
    background: var(--tab);
    border: 5px solid var(--frame);
    border-top: none;
    border-radius: 0 0 72px 72px;
    display: flex; align-items: center; justify-content: center;
  }
  .brand-name {
    color: var(--brand-red);
    font-weight: 700;
    font-size: 30px;
    text-align: center;
    line-height: 1.2;
  }

  .product-title {
    position: absolute; left: 0; right: 0;
    text-align: center;
    color: var(--title);
    font-family: "Great Vibes", cursive;
    font-weight: 400;
    line-height: 1;
    white-space: nowrap;
  }
  .label--oil .product-title { top: 344px; font-size: 104px; }
  .label--lotion .product-title { top: 372px; font-size: 98px; }

  .ingredients { position: absolute; left: 0; right: 0; text-align: center; white-space: nowrap; }
  .label--oil .ingredients {
    top: 863px; color: var(--title); font-size: 16px; line-height: 22px;
  }
  .label--lotion .ingredients {
    top: 846px; color: var(--ink-blue);
    font-size: 10.5px; font-weight: 600; line-height: 16px; letter-spacing: -0.3px;
  }
</style>
</head>
<body>
<main class="canvas">

  <section class="label label--oil">
    <div class="label__photo" role="img" aria-label="Photograph of bay leaves and berries over ripe green and purple olives, with a faint damask pattern"></div>
    <div class="brand-tab"><p class="brand-name">Ferrucci's<br>Bath &amp; Shave</p></div>
    <h1 class="product-title">Bath Oil</h1>
    <p class="ingredients">Ingredients: olive oil, Grapeseed oil and fragrance oil.</p>
  </section>

  <section class="label label--lotion">
    <div class="label__photo" role="img" aria-label="Blue damask pattern background"></div>
    <svg class="label__swirl" viewBox="0 0 493 912" role="img" aria-label="Photograph of a flowing swirl of cream lotion">
      <defs>
        <linearGradient id="creamFlow" x1="0" y1="0" x2="1" y2="1">
          <stop offset="0" stop-color="#f3ecdc"/>
          <stop offset="0.6" stop-color="#e2d6bd"/>
          <stop offset="1" stop-color="#f3ecdc"/>
        </linearGradient>
      </defs>
      <path d="M0 476 C150 492 350 620 493 790 L493 912 L0 912 Z" fill="url(#creamFlow)"/>
    </svg>
    <div class="brand-tab"><p class="brand-name">Ferrucci's<br>Bath &amp; Shave</p></div>
    <h1 class="product-title">Body Lotion</h1>
    <p class="ingredients">Ingredients: Water, Olive Oil, Aloe Vera Juice, Avocado Oil, Rice Bran Oil,<br>BTMS-50, Glycerin, Stearyl Alchohol, Oat Extract, DL Panthenol, Presevane, Buckthorn Extract,<br>Vitamin E and Fragrance oil</p>
  </section>

</main>
</body>
</html>
```